Kestrel Photography Business Card

I need a business card designed for a photography business based in Perth, Western Australia called Kestrel Photography.

We specialise in wedding, event photography and portrait photography.

The business card must borrow the style of the attached logo.

The hex codes for the colours in the logo are:
#ED1D85 - Pink
#89C23E - Green
#37282F - Black

The name on the card will be:
Name: Toviran
Phone: 0417395268
Website: www.kestrelphotography.com.au
Facebook: kestrelphotography

I am open and happy to accept creative concepts.

I’d like some space at the back for writing notes and appointment details.

```html
<!DOCTYPE html>
<html lang="en">
<head>
<meta charset="utf-8">
<title>Kestrel Photography Business Card</title>
<link rel="stylesheet" href="https://fonts.googleapis.com/css2?family=Didact+Gothic&display=swap">
<style>
  :root {
    --pink: #ED1D85;
    --green: #89C23E;
    --ink: #37282F;
    --text-grey: #6f676b;
    --rule-grey: #8a8487;
    --card: #f8f8f6;
    --surface: #e4e4e4;
  }
  * { box-sizing: border-box; margin: 0; padding: 0; }
  html, body { width: 1200px; height: 720px; overflow: hidden; }
  body {
    background: var(--surface);
    font-family: "Didact Gothic", "Helvetica Neue", Arial, sans-serif;
    color: var(--text-grey);
    display: flex;
    align-items: center;
    justify-content: center;
    gap: 40px;
  }
  .card {
    position: relative;
    width: 540px;
    height: 310px;
    background: var(--card);
    border-bottom: 4px solid var(--pink);
  }

  /* Front */
  .brand {
    position: absolute;
    top: 34px;
    left: 0;
    right: 0;
    display: flex;
    flex-direction: column;
    align-items: center;
    gap: 20px;
  }
  .brand-dot {
    width: 52px;
    height: 52px;
    border-radius: 50%;
    border: 3px solid var(--pink);
  }
  .brand-name {
    font-size: 13px;
    letter-spacing: 0.62em;
    text-transform: uppercase;
    color: var(--text-grey);
    padding-left: 0.62em;
  }
  .person-name {
    position: absolute;
    top: 160px;
    left: 0;
    right: 0;
    text-align: center;
    font-size: 20px;
    letter-spacing: 0.06em;
    text-transform: uppercase;
    color: var(--text-grey);
  }
  .contacts {
    position: absolute;
    left: 30px;
    right: 30px;
    bottom: 34px;
    display: flex;
    justify-content: space-between;
    align-items: center;
    list-style: none;
    font-size: 10.5px;
    letter-spacing: 0.03em;
    color: var(--text-grey);
  }
  .contact { display: flex; align-items: center; gap: 8px; }
  .contact-icon {
    width: 14px;
    height: 14px;
    flex: none;
  }

  /* Back */
  .back-brand {
    position: absolute;
    top: 40px;
    left: 0;
    right: 0;
    display: flex;
    justify-content: center;
    align-items: center;
    gap: 12px;
  }
  .back-brand .brand-dot { width: 40px; height: 40px; }
  .back-brand .brand-name { font-size: 11px; letter-spacing: 0.5em; }
  .note-lines {
    position: absolute;
    left: 34px;
    right: 34px;
    top: 128px;
    display: flex;
    flex-direction: column;
    gap: 24px;
  }
  .note-line {
    height: 1px;
    background: var(--rule-grey);
  }
</style>
</head>
<body>

  <section class="card card-front" aria-label="Business card front">
    <div class="brand">
      <span class="brand-dot"></span>
      <span class="brand-name">Kestrel Photography</span>
    </div>
    <p class="person-name">Toviran</p>
    <ul class="contacts">
      <li class="contact">
        <svg class="contact-icon" viewBox="0 0 14 14" aria-hidden="true">
          <circle cx="7" cy="7" r="7" fill="var(--ink)"/>
          <rect x="4.5" y="3.5" width="5" height="7" rx="0.8" fill="none" stroke="#fff" stroke-width="1"/>
        </svg>
        <span>0417395268</span>
      </li>
      <li class="contact">
        <svg class="contact-icon" viewBox="0 0 14 14" aria-hidden="true">
          <circle cx="7" cy="7" r="7" fill="var(--ink)"/>
          <circle cx="7" cy="7" r="3.6" fill="none" stroke="#fff" stroke-width="0.9"/>
          <ellipse cx="7" cy="7" rx="1.5" ry="3.6" fill="none" stroke="#fff" stroke-width="0.8"/>
          <line x1="3.4" y1="7" x2="10.6" y2="7" stroke="#fff" stroke-width="0.8"/>
        </svg>
        <span>www.kestrelphotography.com.au</span>
      </li>
      <li class="contact">
        <svg class="contact-icon" viewBox="0 0 14 14" aria-hidden="true">
          <circle cx="7" cy="7" r="7" fill="var(--ink)"/>
        </svg>
        <span>kestrelphotography</span>
      </li>
    </ul>
  </section>

  <section class="card card-back" aria-label="Business card back with note lines">
    <div class="back-brand">
      <span class="brand-dot"></span>
      <span class="brand-name">Kestrel Photography</span>
    </div>
    <div class="note-lines">
      <div class="note-line"></div>
      <div class="note-line"></div>
      <div class="note-line"></div>
      <div class="note-line"></div>
      <div class="note-line"></div>
    </div>
  </section>

</body>
</html>
```